Website for Cedar Brook Fellowship Church

Wordpress website design required for Cedar Brook Fellowship Church. We are a family oriented church catering for age groups from school age to elderly people. The church has a wide variety of activities which it coordinates. The idea is to describe the activities on the activities page, but cross-link them to show which would be applicable to the different age groups.

We would like an inviting website which is easy to read and navigate.

Target Market(s)

Very wide audience - from school age youth to elderly people, so design and style should cater for both audiences.

Industry/Entity Type

Church

Coding

Coded - Design and coding required

Number of Pages Required

5+ page

Font styles to use
Sans Serif

Colors
0255a3
ffffff
0792cd
f78f20

Requirements
Must have
• Inviting website.
• Clear readable font.
• Space to import photos to balance text on each page.
• Need to project a dynamic and progressive feel for the church.
• Easy to navigate.
Nice to have
• Scrolling photos on pages. Ability to enter questions/ comments/prayer requests on Home page.
Should not have
• Conservative audience, so should not be too bold.

```html
<!DOCTYPE html>
<html lang="en">
<head>
<meta charset="utf-8">
<title>Cedar Brook Fellowship Church</title>
<link href="https://fonts.googleapis.com/css2?family=Open+Sans:wght@400;600;700&family=Roboto:wght@300;400;500&display=swap" rel="stylesheet">
<style>
:root{
  --blue:#0255a3;
  --blue-dark:#0a3f86;
  --sky:#0792cd;
  --orange:#f78f20;
  --orange-light:#fbb066;
  --white:#ffffff;
  --peach:#fdebd7;
  --grey-bg:#f3f3f3;
  --text:#444444;
  --heading:#1c1c1c;
  --line:#e2d3c2;
}
*{box-sizing:border-box;margin:0;padding:0}
html,body{width:1200px;height:3830px;overflow:hidden;background:var(--white)}
body{font-family:"Open Sans",Arial,sans-serif;color:var(--text);position:relative}
.section{position:absolute;left:0;width:1200px;overflow:hidden}
.abs{position:absolute}
.h-title{font-family:"Roboto",Arial,sans-serif;font-weight:300;color:var(--blue);font-size:32px}
.body-copy{font-size:12.5px;line-height:20px;color:var(--text)}
.btn{position:absolute;display:flex;align-items:center;justify-content:center;color:var(--white);font-family:"Open Sans",Arial,sans-serif;font-size:12px;font-weight:600;letter-spacing:.5px}
.btn-blue{background:var(--blue)}
.btn-orange{background:var(--orange)}

/* header */
.site-header{top:0;height:122px;border-top:4px solid var(--orange);background:var(--white)}
.brand{left:102px;top:30px;display:flex;align-items:center;gap:10px}
.brand-dot{width:34px;height:34px;border-radius:50%;background:var(--orange)}
.brand-name{font-family:"Roboto",Arial,sans-serif;font-size:20px;font-weight:400;color:var(--blue)}
.partner-badge{right:98px;top:38px;width:58px;height:58px;border-radius:50%;background:#2a2a2a}
.main-nav{top:122px;height:52px;background:var(--blue)}
.nav-list{display:flex;height:52px;margin-left:102px;list-style:none}
.nav-list li{display:flex;align-items:center;padding:0 16px;color:var(--white);font-size:12.5px;font-weight:600;letter-spacing:.3px}
.nav-list li.active{background:var(--orange)}
.nav-caret{margin-left:6px;font-size:9px}
.nav-search{right:108px;top:17px}

/* hero */
.hero{top:174px;height:485px}
.hero-photo{position:absolute;inset:0;background:linear-gradient(100deg,#9a6a3b 0%,#c89a62 35%,#e6c89c 60%,#b98a55 100%)}
.service-card{left:97px;top:69px;width:403px;height:339px;background:var(--white);box-shadow:0 2px 8px rgba(0,0,0,.2)}
.card-band{position:absolute;left:0;top:43px;width:403px;height:56px}
.card-band-title{position:absolute;right:44px;top:52px;font-family:"Roboto",Arial,sans-serif;font-weight:300;font-size:29px;color:var(--white)}
.service-row{position:absolute;left:17px;display:flex;width:370px;font-family:"Roboto",Arial,sans-serif;font-size:19px;color:var(--heading);padding-bottom:12px}
.service-row .time{width:122px;font-weight:500}
.service-row .name{font-weight:300}
.service-row.first{top:134px;border-bottom:1px solid #e6e6e6}
.service-row.second{top:195px}

/* welcome */
.welcome{top:659px;height:375px;background:var(--white)}

/* activities */
.activities{top:1034px;height:569px;background:var(--peach)}
.section-rule{position:absolute;left:97px;width:1003px;height:1px;background:var(--line)}
.slider-arrows{right:100px;display:flex;gap:24px;color:var(--blue)}
.activity-card{position:absolute;top:153px;width:317px;height:332px;background:var(--white);box-shadow:0 1px 4px rgba(0,0,0,.12)}
.activity-photo{height:261px}
.activity-name{padding:18px 14px;font-family:"Roboto",Arial,sans-serif;font-weight:500;font-size:20px;color:var(--heading)}
.photo-warm{background:linear-gradient(135deg,#7a3a2c,#c4614e 50%,#e6b89a)}
.photo-room{background:linear-gradient(135deg,#6d6258,#b3a79b 50%,#e1ddd6)}
.photo-garden{background:linear-gradient(135deg,#4f6a3a,#a9a07a 50%,#d8cfb5)}

/* prayer & mission */
.prayer-mission{top:1603px;height:483px;background:var(--white)}
.prayer-panel{left:0;top:0;width:500px;height:483px;background:linear-gradient(160deg,#2f78c4 0%,var(--blue) 55%,#0a4a93 100%)}
.prayer-band{position:absolute;left:0;top:77px}
.prayer-band-title{position:absolute;right:88px;top:87px;font-family:"Roboto",Arial,sans-serif;font-weight:300;font-size:29px;color:var(--white)}
.field{position:absolute;background:var(--white);border:1px solid #d9d9d9;font-size:11px;color:#9a9a9a;padding:8px 10px}
.mission-lead{left:528px;top:148px;width:540px;font-family:"Roboto",Arial,sans-serif;font-weight:500;font-size:19px;line-height:25px;color:var(--heading)}

/* news */
.news{top:2086px;height:664px;background:var(--grey-bg)}
.news-card{position:absolute;top:153px;width:317px;height:424px;background:var(--white);box-shadow:0 1px 4px rgba(0,0,0,.1)}
.news-photo{height:199px}
.news-body{padding:24px 14px 0}
.news-title{font-family:"Roboto",Arial,sans-serif;font-weight:500;font-size:19px;line-height:22px;color:var(--heading);height:60px}
.news-excerpt{font-size:11.5px;line-height:19px;color:#666;margin-top:8px}
.news-meta{position:absolute;left:14px;right:14px;bottom:0;height:56px;border-top:1px solid #e6e6e6;display:flex;justify-content:space-between;align-items:center;font-size:11.5px;color:#777}
.news-more{color:var(--blue);font-weight:700}
.photo-dinner{background:linear-gradient(135deg,#5c4336,#a9836d 50%,#d9c6b6)}
.photo-building{background:linear-gradient(180deg,#1c57b8 0%,#4a86d6 45%,#b89a6c 60%,#7c5a38 100%)}
.photo-kitchen{background:linear-gradient(135deg,#6b6b5c,#b6b09a 50%,#e5e2d6)}

/* message & contact */
.message{top:2750px;height:613px;background:var(--white)}
.quote{left:97px;top:150px;width:555px;font-size:12.5px;line-height:20px}
.pastor-photo{left:301px;top:270px;width:168px;height:168px;border-radius:50%;background:radial-gradient(circle at 50% 40%,#d7d3ce,#9aa2ab);border:4px solid #eeeeee}
.pastor-name{left:97px;top:452px;width:576px;text-align:center;font-weight:700;font-size:14px;color:var(--heading)}
.contact-panel{left:700px;top:0;width:500px;height:613px;background:linear-gradient(135deg,#e8a060 0%,#d9822f 45%,#c76f1d 100%)}
.contact-band{position:absolute;left:0;top:74px}
.contact-band-title{position:absolute;left:44px;top:84px;font-family:"Roboto",Arial,sans-serif;font-weight:300;font-size:29px;color:var(--white)}

/* social */
.social{top:3363px;height:147px;background:#f1f1f1}
.social-title{left:97px;top:42px;font-family:"Roboto",Arial,sans-serif;font-weight:500;font-size:30px;color:var(--blue)}
.social-sub{left:97px;top:84px;font-size:12px;color:var(--text)}

/* footer */
.contact-strip{top:3510px;height:261px;background:radial-gradient(circle at 30% 30%,#2e6fc2 0%,var(--blue-dark) 45%,#06306a 100%)}
.contact-item{position:absolute;top:55px;width:340px;text-align:center;color:var(--white);font-size:19px;line-height:24px}
.contact-item svg{display:block;margin:0 auto 22px}
.copyright{top:3771px;height:59px;background:var(--orange);display:flex;align-items:center;padding-left:97px;font-size:11px;font-weight:700;color:#3a2a10}
</style>
</head>
<body>

<header class="section site-header">
  <div class="abs brand">
    <span class="brand-dot"></span>
    <span class="brand-name">Cedar Brook Fellowship Church</span>
  </div>
  <div class="abs partner-badge"></div>
</header>

<nav class="section main-nav">
  <ul class="nav-list">
    <li class="active">HOME</li>
    <li>AGE GROUP</li>
    <li>ACTIVITIES<span class="nav-caret">&#9660;</span></li>
    <li>EVENTS CALENDAR</li>
    <li>ABOUT</li>
    <li>CONTACT</li>
  </ul>
  <svg class="abs nav-search" width="18" height="18" viewBox="0 0 18 18"><circle cx="7.5" cy="7.5" r="5" fill="none" stroke="#fff" stroke-width="2"/><line x1="11" y1="11" x2="15.5" y2="15.5" stroke="#fff" stroke-width="2.4" stroke-linecap="round"/></svg>
</nav>

<section class="section hero">
  <div class="hero-photo" role="img" aria-label="Young girl praying in a golden wheat field"></div>
  <div class="abs service-card">
    <svg class="card-band" width="403" height="56" viewBox="0 0 403 56"><polygon points="0,0 58,0 74,28 58,56 0,56 10,28" fill="#fbb066"/><polygon points="68,0 403,0 403,56 68,56 84,28" fill="#f78f20"/></svg>
    <div class="card-band-title">Service Times</div>
    <div class="service-row first"><span class="time">08:00 AM</span><span class="name">Traditional Worship Service</span></div>
    <div class="service-row second"><span class="time">10:00 AM</span><span class="name">Family Worship Service</span></div>
    <div class="btn btn-blue" style="left:18px;top:255px;width:115px;height:43px">VIEW ALL</div>
  </div>
</section>

<section class="section welcome">
  <h1 class="abs h-title" style="left:97px;top:80px">Welcome to Cedar Brook Fellowship Church</h1>
  <p class="abs body-copy" style="left:97px;top:150px;width:1003px">Lorem ipsum dolor sit amet, consectetuer adipiscing elit, sed diam nonummy nibh euismod tincidunt ut laoreet dolore magna aliquam erat volutpat. Ut wisi enim ad minim veniam, quis nostrud exerci tation ullamcorper suscipit lobortis nisl ut aliquip ex ea commodo consequat. Duis autem vel eum iriure dolor in hendrerit in vulputate velit esse molestie consequat.</p>
  <p class="abs body-copy" style="left:97px;top:220px;width:1003px">Vel illum dolore eu feugiat nulla facilisis at vero eros et accumsan et iusto odio dignissim qui blandit praesent luptatum zzril delenit augue duis dolore te feugait nulla facilisi. Nam liber tempor cum soluta nobis eleifend option congue nihil imperdiet doming id quod mazim placerat facer possim assum. Typi non habent claritatem insitam; est usus legentis in iis qui facit eorum claritatem. Investigationes demonstraverunt lectores legere me lius quod ii legunt saepius. Claritas est etiam processus dynamicus, qui sequitur mutationem consuetudium lectorum.</p>
</section>

<section class="section activities">
  <h2 class="abs h-title" style="left:97px;top:82px">Activities</h2>
  <div class="abs slider-arrows" style="top:88px">
    <svg width="14" height="20" viewBox="0 0 14 20"><polyline points="11,2 3,10 11,18" fill="none" stroke="currentColor" stroke-width="3"/></svg>
    <svg width="14" height="20" viewBox="0 0 14 20"><polyline points="3,2 11,10 3,18" fill="none" stroke="currentColor" stroke-width="3"/></svg>
  </div>
  <div class="section-rule" style="top:133px"></div>
  <article class="activity-card" style="left:97px">
    <div class="activity-photo photo-warm" role="img" aria-label="Children and parents gathered at playgroup"></div>
    <h3 class="activity-name">Little Sprouts Playgroup</h3>
  </article>
  <article class="activity-card" style="left:442px">
    <div class="activity-photo photo-room" role="img" aria-label="Women enjoying coffee together in the hall"></div>
    <h3 class="activity-name">Ladies Coffee Group</h3>
  </article>
  <article class="activity-card" style="left:784px">
    <div class="activity-photo photo-garden" role="img" aria-label="Men standing together outdoors with coffee"></div>
    <h3 class="activity-name">Mens Coffee Group</h3>
  </article>
</section>

<section class="section prayer-mission">
  <div class="abs prayer-panel" role="img" aria-label="Blue tinted background of praying hands">
    <svg class="prayer-band" width="460" height="56" viewBox="0 0 460 56"><polygon points="0,0 60,0 76,28 60,56 0,56" fill="#fbb066"/><polygon points="70,0 460,0 460,56 70,56 86,28" fill="#f78f20"/></svg>
    <div class="prayer-band-title">Prayer Request</div>
    <div class="field" style="left:143px;top:197px;width:314px;height:140px">Your prayer request</div>
    <div class="btn btn-orange" style="left:342px;top:353px;width:115px;height:43px">SUBMIT</div>
  </div>
  <h2 class="abs h-title" style="left:528px;top:82px">Our Mission</h2>
  <div class="abs" style="left:528px;top:130px;width:572px;height:1px;background:#e6e6e6"></div>
  <p class="abs mission-lead">Our mission is to reflect the love of God as revealed in Jesus and through His Spirit to make him known by word, sign and deed</p>
  <p class="abs body-copy" style="left:528px;top:240px;width:572px;font-size:12px;line-height:19px">Claritas est etiam processus dynamicus, qui sequitur mutationem consuetudium lectorum. Mirum est notare quam littera gothica, quam nunc putamus parum claram, anteposuerit litterarum formas humanitatis per seacula quarta decima et quinta decima. Eodem modo typi, qui nunc nobis videntur parum clari, fiant sollemnes in futurum.</p>
  <div class="btn btn-blue" style="left:531px;top:358px;width:115px;height:43px">READ MORE</div>
</section>

<section class="section news">
  <h2 class="abs h-title" style="left:97px;top:82px">News</h2>
  <div class="abs slider-arrows" style="top:88px">
    <svg width="14" height="20" viewBox="0 0 14 20"><polyline points="11,2 3,10 11,18" fill="none" stroke="currentColor" stroke-width="3"/></svg>
    <svg width="14" height="20" viewBox="0 0 14 20"><polyline points="3,2 11,10 3,18" fill="none" stroke="currentColor" stroke-width="3"/></svg>
  </div>
  <div class="section-rule" style="top:133px;background:#dddddd"></div>
  <article class="news-card" style="left:97px">
    <div class="news-photo photo-dinner" role="img" aria-label="Members sharing a meal at a long table"></div>
    <div class="news-body">
      <h3 class="news-title">Claritas est etiam processus dynamicus sequitur</h3>
      <p class="news-excerpt">Duis autem vel eum iriure dolor in hendrerit in vulputate velit esse molestie consequat, vel illum dolore eu feugiat nulla facilisis at vero eros.</p>
    </div>
    <div class="news-meta"><span>&#128197; Nov 1, 2016</span><span class="news-more">Read more &#9656;</span></div>
  </article>
  <article class="news-card" style="left:442px">
    <div class="news-photo photo-building" role="img" aria-label="Church building with a cross under a blue sky"></div>
    <div class="news-body">
      <h3 class="news-title">Typi non habent claritatem insitam</h3>
      <p class="news-excerpt">Duis autem vel eum iriure dolor in hendrerit in vulputate velit esse molestie consequat, vel illum dolore eu feugiat nulla facilisis at vero eros.</p>
    </div>
    <div class="news-meta"><span>&#128197; Oct 31, 2016</span><span class="news-more">Read more &#9656;</span></div>
  </article>
  <article class="news-card" style="left:784px">
    <div class="news-photo photo-kitchen" role="img" aria-label="Volunteers preparing food in the church kitchen"></div>
    <div class="news-body">
      <h3 class="news-title">Duis autem veleum iriurenh dolor</h3>
      <p class="news-excerpt">Duis autem vel eum iriure dolor in hendrerit in vulputate velit esse molestie consequat, vel illum dolore eu feugiat nulla facilisis at vero eros.</p>
    </div>
    <div class="news-meta"><span>&#128197; Oct 22, 2016</span><span class="news-more">Read more &#9656;</span></div>
  </article>
</section>

<section class="section message">
  <h2 class="abs h-title" style="left:97px;top:80px">Message</h2>
  <div class="abs" style="left:97px;top:128px;width:576px;height:1px;background:#e6e6e6"></div>
  <p class="abs body-copy quote">“Lorem ipsum dolor sit amet, consectetuer adipiscing elit, sed diam nonummy nibh euismod tincidunt ut laoreet dolore magna aliquam erat volutpat. Ut wisi enim ad minim veniam, quis nostrud exerci tation ullamcorper suscipit lobortis nisl ut aliquip ex ea commodo consequat. Duis autem vel eum iriure dolor in hendrerit in vulputate velit esse molestie consequat.”</p>
  <div class="abs pastor-photo" role="img" aria-label="Portrait of the church reverend"></div>
  <div class="abs pastor-name">Reverend Alan Hartley</div>
  <div class="abs contact-panel" role="img" aria-label="Warm orange background of open hands">
    <svg class="contact-band" width="500" height="56" viewBox="0 0 500 56"><polygon points="0,0 413,0 397,28 413,56 0,56" fill="#0255a3"/><polygon points="423,0 500,0 500,56 423,56 407,28" fill="#fbb066"/></svg>
    <div class="contact-band-title">Get in Touch</div>
    <div class="field" style="left:43px;top:196px;width:314px;height:41px">Name</div>
    <div class="field" style="left:43px;top:252px;width:314px;height:41px">Email</div>
    <div class="field" style="left:43px;top:308px;width:314px;height:41px">Subject</div>
    <div class="field" style="left:43px;top:367px;width:314px;height:141px">Message</div>
    <div class="btn btn-blue" style="left:242px;top:523px;width:115px;height:41px">SUBMIT</div>
  </div>
</section>

<section class="section social">
  <h2 class="abs social-title">We are on Wovenpage</h2>
  <p class="abs social-sub">Typi non habent claritatem insitamest usus legentis in iis qui facit eorum claritatem.</p>
  <div class="btn btn-blue" style="left:916px;top:50px;width:184px;height:41px;font-size:11px"><span style="display:inline-block;width:11px;height:11px;background:#fff;margin-right:6px"></span>LIKE US ON WOVENPAGE</div>
</section>

<footer class="section contact-strip">
  <div class="contact-item" style="left:85px">
    <svg width="40" height="52" viewBox="0 0 40 52"><path d="M20 3C11 3 4 10 4 19c0 12 16 29 16 29s16-17 16-29C36 10 29 3 20 3z" fill="none" stroke="#fff" stroke-width="2.5"/><circle cx="20" cy="19" r="6" fill="none" stroke="#fff" stroke-width="2.5"/></svg>
    14 Willow Lane, Cedar Brook,<br>6200 Australia
  </div>
  <div class="contact-item" style="left:427px">
    <svg width="52" height="52" viewBox="0 0 52 52"><path d="M14 5l8 10-5 6c3 7 8 12 14 15l6-5 10 8-5 7C28 46 6 24 7 10z" fill="none" stroke="#fff" stroke-width="2.5" stroke-linejoin="round"/></svg>
    +61 9000 4127
  </div>
  <div class="contact-item" style="left:770px">
    <svg width="58" height="52" viewBox="0 0 58 52"><rect x="3" y="9" width="52" height="34" fill="none" stroke="#fff" stroke-width="2.5"/><polyline points="3,9 29,30 55,9" fill="none" stroke="#fff" stroke-width="2.5"/><line x1="3" y1="43" x2="22" y2="24" stroke="#fff" stroke-width="2.5"/><line x1="55" y1="43" x2="36" y2="24" stroke="#fff" stroke-width="2.5"/></svg>
    office@cedarbrookchurch.org
  </div>
</footer>

<div class="section copyright">Copyright © 2016&nbsp;<span style="color:var(--blue)">Cedar Brook Fellowship Church</span></div>

</body>
</html>
```